Brightwater Ledger Services, Inc.

Tax, Accounting and Bookkeeping Services

“We provide our services, with you next mortgage in mind”

Special pricing available for all Mortgage Loan Customers!!

President / CEO Marcus Delaney

Primary service provider with over 27 years of experience

Call directly for more information: (240) 555-0182

Or email at: mdelaney@brightwaterledger-example.com

```html
<!DOCTYPE html>
<html lang="en">
<head>
<meta charset="utf-8">
<title>Brightwater Ledger Services – Mortgage Customers</title>
<link href="https://fonts.googleapis.com/css2?family=Poppins:wght@500;600;800&family=Open+Sans:ital,wght@1,400;1,600;1,700;1,800&display=swap" rel="stylesheet">
<style>
  :root {
    --mat: #a9a9a9;
    --paper: #ffffff;
    --gold-dark: #6b5410;
    --gold-mid: #c9a126;
    --gold-light: #ebd348;
    --gold-text: #e6be2e;
    --blue-top: #00579a;
    --blue-bottom: #02182f;
    --blue-card: #005496;
    --white: #ffffff;
  }
  * { box-sizing: border-box; margin: 0; padding: 0; }
  html, body { width: 1197px; height: 1200px; overflow: hidden; background: var(--mat); }
  .canvas { position: relative; width: 1197px; height: 1200px; background: var(--mat); }
  .flyer { position: absolute; left: 80px; top: 71px; width: 1051px; height: 1054px; background: var(--paper); overflow: hidden; }
  .abs { position: absolute; }

  .photo-sky { left: 520px; top: 0; width: 531px; height: 62px;
    background: linear-gradient(90deg, #ffffff 0%, #eef0f2 25%, #eef0f2 100%); }
  .photo { left: 528px; top: 62px; width: 523px; height: 762px;
    background:
      linear-gradient(90deg, #ffffff 0%, rgba(255,255,255,0) 22%),
      linear-gradient(180deg, rgba(255,255,255,0) 80%, #ffffff 100%),
      linear-gradient(160deg, #f4f5f6 0%, #e3e4e7 35%, #cfd1d5 60%, #e9eaec 80%, #f3f4f5 100%);
  }

  .brand { left: 40px; top: 48px; display: flex; align-items: center; gap: 12px;
    font-family: "Poppins", sans-serif; font-weight: 800; font-size: 23px; line-height: 1.15; color: var(--blue-card); width: 320px; }
  .brand-dot { flex: none; width: 40px; height: 40px; border-radius: 50%; background: var(--gold-mid); }

  .gold-band { left: 0; top: 188px; width: 696px; height: 258px;
    background: linear-gradient(90deg, var(--gold-dark) 0%, #a47e18 40%, var(--gold-mid) 70%, var(--gold-light) 100%); }
  .services { left: 32px; top: 218px; font-family: "Poppins", sans-serif; font-weight: 500; font-size: 18px; color: var(--white); }
  .headline { left: 32px; top: 244px; font-family: "Poppins", sans-serif; font-weight: 600; font-size: 53px; line-height: 60px; color: var(--white); letter-spacing: -0.8px; }

  .blue-panel { left: 0; top: 446px; width: 521px; height: 608px;
    background: linear-gradient(180deg, var(--blue-top) 0%, #003f74 45%, var(--blue-bottom) 100%); }
  .fold { left: 521px; top: 446px; }

  .offer { left: 28px; top: 487px; font-family: "Open Sans", sans-serif; font-style: italic; font-weight: 400; font-size: 40px; line-height: 52px; color: var(--white); letter-spacing: -0.8px; }

  .headshot { left: 81px; top: 685px; width: 157px; height: 157px; border-radius: 26px;
    background: linear-gradient(160deg, #d9dadc 0%, #a5a7ab 55%, #2b2b2f 100%); }
  .leader { left: 271px; top: 731px; font-family: "Poppins", sans-serif; font-weight: 800; font-size: 19px; line-height: 23px; color: var(--white); }
  .leader .name { color: var(--gold-text); display: block; }

  .experience { left: 60px; top: 870px; width: 460px; font-family: "Open Sans", sans-serif; font-style: italic; color: var(--white); }
  .exp-lines { position: absolute; left: 0; top: 3px; width: 251px; text-align: right; font-size: 31px; line-height: 34px; letter-spacing: -0.8px; white-space: nowrap; }
  .exp-number { position: absolute; left: 266px; top: -14px; font-size: 92px; font-weight: 800; color: var(--gold-text); letter-spacing: -4px; line-height: 1; }
  .exp-years { position: absolute; left: 0; top: 74px; font-size: 41px; letter-spacing: -1px; line-height: 1.2; white-space: nowrap; }

  .contact-shape { left: 0; top: 0; }
  .phone-icon { left: 669px; top: 920px; }
  .contact { left: 762px; top: 918px; font-family: "Open Sans", sans-serif; font-style: italic; color: var(--white); }
  .contact .label { font-size: 15px; font-weight: 600; letter-spacing: -0.3px; }
  .contact .number { font-size: 35px; font-weight: 800; letter-spacing: -0.8px; line-height: 44px; }
  .contact .email { font-size: 11.6px; font-weight: 600; letter-spacing: -0.2px; margin-left: -6px; white-space: nowrap; }
</style>
</head>
<body>
<div class="canvas">
  <div class="flyer">
    <div class="abs photo-sky"></div>
    <div class="abs photo" role="img" aria-label="Photo of a couple at a bright kitchen table reviewing papers with a calculator, coffee cup and phone"></div>

    <div class="abs brand"><span class="brand-dot"></span><span>Brightwater Ledger Services, Inc.</span></div>

    <div class="abs gold-band"></div>
    <p class="abs services">Tax, Accounting and Bookkeeping Services</p>
    <h1 class="abs headline">We provide our services<br>with you next<br>mortgage in mind</h1>

    <div class="abs blue-panel"></div>
    <svg class="abs fold" width="175" height="123" viewBox="0 0 175 123" aria-hidden="true">
      <defs>
        <linearGradient id="foldGrad" x1="0" y1="0" x2="0" y2="1">
          <stop offset="0" stop-color="#050505"/>
          <stop offset="1" stop-color="#8a7420"/>
        </linearGradient>
      </defs>
      <polygon points="0,0 175,0 0,123" fill="url(#foldGrad)"/>
    </svg>

    <p class="abs offer">&nbsp;Special pricing available<br>for all Mortgage Loan<br>Customers!!</p>

    <div class="abs headshot" role="img" aria-label="Portrait photo of the company president in a black hat and suit"></div>
    <p class="abs leader">President / CEO<span class="name">Marcus Delaney</span></p>

    <div class="abs experience">
      <p class="exp-lines">Primary service<br>provider with over</p>
      <p class="exp-number">27</p>
      <p class="exp-years">Years of Experience</p>
    </div>

    <svg class="abs contact-shape" width="1051" height="1054" viewBox="0 0 1051 1054" aria-hidden="true">
      <polygon points="550,1054 550,898 721,816 1051,816 1051,1054" fill="#cfa426"/>
      <polygon points="584,1054 584,926 758,842 1051,842 1051,1054" fill="var(--blue-card)"/>
    </svg>
    <svg class="abs phone-icon" width="72" height="72" viewBox="0 0 72 72" aria-hidden="true">
      <circle cx="36" cy="36" r="33" fill="none" stroke="#fff" stroke-width="3"/>
      <path d="M24 20c2-1.5 4-1 5 1l3 6c.8 1.6.3 3-1 4l-2 1.6c1.6 4 5 7.6 9 9.4l1.7-2c1-1.2 2.6-1.6 4-.8l6 3.2c2 1 2.2 3 .8 5-2.4 3.2-6 4.6-10 3-8-3.2-15-10.4-18-18.6-1.4-4.4.2-8.6 1.5-10.8z" fill="#fff"/>
      <path d="M39 22a11 11 0 0 1 11 11M40 15a18 18 0 0 1 17 17M41 29a4 4 0 0 1 2 4" fill="none" stroke="#fff" stroke-width="2.6" stroke-linecap="round"/>
    </svg>
    <div class="abs contact">
      <p class="label">Call directly for more information:</p>
      <p class="number">(240) 555-0182</p>
      <p class="email">Or email at: mdelaney@brightwaterledger-example.com</p>
    </div>
  </div>
</div>
</body>
</html>
```